Mental Health Awareness License Plates

Below is the sample format I will need. That of a plain license plate w/o frame
*refer to image with name Licence wo Frame*
Delete Frame
Replace QR Code with “MO”
Replace 2025 sticker with “ YR
Use License Plate font (attached)
On Ribbon, keep the green background
The California front leg, needs to be gradated like a sunset and retain shape of CA
Palm trees sharpened
I need the files in a format that can be used on a website, printed or made into a poster.
One file that reads SAMPLE, one version that reads “NEWPLA8”d
The finished product should look like a license plate as shown in the example
*refer to image name finished product*
I want to clarify what we are looking for. The license plate design has been approved by the state, but we need a high res version of it in multiple file formats. The most important change we are looking for is to the ribbon. The palm trees against the sunset are fuzzy, we need those placed in front of an sunset on the front leg of the ribbon. The rear leg needs to remain green (mental health color). I hope this help clarify our design need.

```html
<!DOCTYPE html>
<html lang="en">
<head>
<meta charset="UTF-8">
<title>Mental Health Awareness License Plate</title>
<link href="https://fonts.googleapis.com/css2?family=Antonio:wght@600&family=Arimo:wght@700&display=swap" rel="stylesheet">
<style>
  :root {
    --page: #ffffff;
    --plate-rim: #ffffff;
    --plate-edge: #8a8a8a;
    --plate-field: #bce2dc;
    --plate-navy: #1e4a6c;
    --state-red: #ea3e4a;
    --sunset-orange: #f26f23;
    --sunset-gold: #f7b21c;
    --sea-blue: #2a86c6;
    --shore-black: #1b1b1b;
  }
  html, body {
    margin: 0;
    padding: 0;
    width: 1200px;
    height: 849px;
    overflow: hidden;
    background: var(--page);
  }
  .plate-canvas {
    display: block;
    width: 1200px;
    height: 849px;
  }
  .plate-rim { fill: var(--plate-rim); stroke: var(--plate-edge); stroke-width: 1; }
  .plate-field { fill: var(--plate-field); }
  .state-name {
    font-family: "Arimo", Arial, sans-serif;
    font-weight: 700;
    font-size: 78px;
    fill: var(--state-red);
  }
  .plate-number {
    font-family: "Antonio", "Arial Narrow", sans-serif;
    font-weight: 600;
    font-size: 195px;
    fill: var(--plate-navy);
  }
  .plate-tagline {
    font-family: "Arimo", Arial, sans-serif;
    font-weight: 700;
    font-size: 28px;
    fill: var(--plate-navy);
  }
</style>
</head>
<body>
<svg class="plate-canvas" viewBox="0 0 1200 849" xmlns="http://www.w3.org/2000/svg">
  <defs>
    <linearGradient id="ribbon-sunset" x1="0" y1="0" x2="0" y2="1">
      <stop offset="0" stop-color="var(--sunset-orange)"/>
      <stop offset="0.5" stop-color="var(--sunset-gold)"/>
      <stop offset="0.7" stop-color="var(--sea-blue)"/>
      <stop offset="0.85" stop-color="var(--shore-black)"/>
      <stop offset="1" stop-color="var(--shore-black)"/>
    </linearGradient>
  </defs>

  <rect class="plate-rim" x="185.5" y="193.5" width="840" height="424" rx="40"/>
  <rect class="plate-field" x="203" y="213" width="806" height="384" rx="27"/>

  <rect class="awareness-ribbon" x="236" y="304" width="131" height="247" rx="40"
        fill="url(#ribbon-sunset)" role="img"
        aria-label="Awareness ribbon filled with a sunset beach scene with palm trees"/>

  <text class="state-name" x="397" y="314" textLength="482" lengthAdjust="spacingAndGlyphs">California</text>

  <text class="plate-number" x="399" y="528" textLength="531" lengthAdjust="spacingAndGlyphs">NEWPL8</text>

  <text class="plate-tagline" x="418" y="573" textLength="397" lengthAdjust="spacingAndGlyphs">MENTAL HEALTH AWARENESS</text>
</svg>
</body>
</html>
```